Billboard - Cool Garden and Landscape Company (Brand Pack Included)

NEED A PROFESSIONAL BILLBOARD TO ADVERTISE OUR BUSINESS. HAVE MOCKED UP A SAMPLE CONCEPT BUT IT REQUIRES THE ICONS TO BE DEVELOPED TO A PROFESSIONAL STANDARD (I JUST COPIED RANDOM EXAMPLES FROM THE NET)

THE ICONS REPRESENT OUR KEY PRODUCT GROUPS. (These can be redesigned)
BILLBOARD IS 6M X 3M (SEE SPEC FILE ATTACHED) - IMAGE OF THE LOCATION ADDED TO THE FILES.

BRAND GUIDE INCLUDED WITH LOGO FILES

VISIT: https://www.facebook.com/Crew.Moss.Crate/
Web: www.mosscrate.co.nz

Target Market(s)

Commuter traffic - busy road - Billboard site is on the left side approx 400m before our street turn off. Age group 30+ Home owners / Builders

Industry/Entity Type

Garden Supply

Font styles to use
Other font styles liked:
• comfortaa

Requirements
Must have
• No change to our logo or brand
• Next left
• Icons for products as per mock up - note these can be redesigned
Nice to have
• Easy to see at a distance
• Clean
• Simple

```html
<!DOCTYPE html>
<html lang="en">
<head>
<meta charset="utf-8">
<title>Moss Crate Billboard</title>
<link rel="stylesheet" href="https://fonts.googleapis.com/css2?family=Comfortaa:wght@500;700&family=Oswald:wght@400;500;600&family=Open+Sans:wght@700&display=swap">
<style>
  :root {
    --backdrop: #666666;
    --paper: #ffffff;
    --green: #2e9e47;
    --orange: #f7941d;
    --ink: #1a1a1a;
    --soil: #5a4636;
    --leaf: #6f9a3e;
  }
  * { margin: 0; padding: 0; box-sizing: border-box; }
  html, body { width: 1200px; height: 1200px; overflow: hidden; }
  body { background: var(--backdrop); position: relative; }

  .billboard {
    position: absolute; left: 109px; top: 355px;
    width: 982px; height: 491px;
    background: var(--paper); overflow: hidden;
  }
  .billboard__art { position: absolute; inset: 0; }

  .directions {
    position: absolute; left: 62px; top: 408px;
    font-family: "Oswald", sans-serif; font-weight: 600;
    font-size: 30px; line-height: 46px; color: var(--green);
    letter-spacing: -0.3px; white-space: nowrap;
  }

  .brand { position: absolute; left: 459px; top: 21px; width: 480px; height: 110px; }
  .brand__mark {
    position: absolute; left: 6px; top: 4px; width: 84px; height: 84px;
    background: var(--green);
  }
  .brand__name {
    position: absolute; left: 110px; top: 20px;
    font-family: "Comfortaa", sans-serif; font-weight: 700;
    font-size: 46px; line-height: 52px; color: var(--green);
    white-space: nowrap; letter-spacing: 0.5px;
  }
  .brand__rule {
    position: absolute; left: 0; top: 96px; width: 203px; height: 3px;
    background: var(--orange);
  }
  .brand__tagline {
    position: absolute; left: 208px; top: 82px;
    font-family: "Comfortaa", sans-serif; font-weight: 500;
    font-size: 21px; line-height: 26px; color: var(--orange);
    white-space: nowrap;
  }

  .product {
    position: absolute; width: 280px; margin-left: -140px;
    text-align: center;
  }
  .product__icon { display: block; margin: 0 auto; }
  .product__label {
    font-family: "Oswald", sans-serif; font-weight: 400;
    font-size: 24px; line-height: 30px; color: var(--ink);
    white-space: nowrap; letter-spacing: -0.4px;
  }
  .product--firewood { left: 604px; top: 150px; }
  .product--compost  { left: 849px; top: 150px; }
  .product--stone    { left: 598px; top: 286px; }
  .product--trailer  { left: 842px; top: 286px; }

  .tagline-band {
    position: absolute; left: 375px; right: 0; top: 431px; height: 60px;
    display: flex; align-items: center; justify-content: center;
    padding-left: 60px;
    font-family: "Open Sans", sans-serif; font-weight: 700;
    font-size: 25px; color: var(--paper);
  }
</style>
</head>
<body>
  <main class="billboard">
    <svg class="billboard__art" width="982" height="491" viewBox="0 0 982 491">
      <defs>
        <linearGradient id="garden-photo" x1="0" y1="0" x2="0.4" y2="1">
          <stop offset="0" stop-color="#6f9a3e"/>
          <stop offset="0.35" stop-color="#6b5a45"/>
          <stop offset="1" stop-color="#4f3d30"/>
        </linearGradient>
      </defs>
      <rect class="band-orange" x="375" y="431" width="607" height="60" fill="var(--orange)"/>
      <path class="arc-green" d="M0 0 H320 Q555 250 300 491 H0 Z" fill="var(--green)"/>
      <path class="arc-orange" d="M0 0 H290 Q540 250 290 491 H0 Z" fill="var(--orange)"/>
      <path class="photo" role="img" aria-label="Photo of a boy in a green cap and orange shirt planting seedlings in a garden bed" d="M0 0 H268 Q510 250 268 491 H0 Z" fill="url(#garden-photo)"/>
      <path class="direction-arrow" d="M27 431 L56 401 L56 412 L359 412 L359 451 L56 451 L56 462 Z" fill="var(--paper)"/>
    </svg>

    <div class="directions">NEXT LEFT 57 Harlow Road</div>

    <div class="brand">
      <div class="brand__mark"></div>
      <div class="brand__name">MOSS CRATE</div>
      <div class="brand__rule"></div>
      <div class="brand__tagline">Create Better Gardens</div>
    </div>

    <div class="product product--firewood">
      <svg class="product__icon" width="70" height="72" viewBox="0 0 70 72">
        <path d="M35 4 C38 16 50 20 50 36 C50 48 43 54 35 54 C27 54 20 48 20 38 C20 30 25 26 27 20 C29 28 31 30 33 30 C31 22 32 12 35 4 Z" fill="var(--orange)"/>
        <path d="M35 26 C37 34 43 38 42 46 C41 50 38 52 35 52 C31 52 28 49 28 45 C28 40 32 38 35 26 Z" fill="var(--paper)"/>
        <rect x="6" y="56" width="58" height="8" rx="4" fill="var(--orange)" transform="rotate(-10 35 60)"/>
        <rect x="6" y="56" width="58" height="8" rx="4" fill="var(--orange)" transform="rotate(10 35 60)"/>
      </svg>
      <div class="product__label">Firewood + Fire Pellets</div>
    </div>

    <div class="product product--compost">
      <svg class="product__icon" width="90" height="72" viewBox="0 0 90 72">
        <path d="M45 62 V14" stroke="var(--green)" stroke-width="4" fill="none"/>
        <path d="M45 16 C40 10 40 4 45 0 C50 4 50 10 45 16 Z" fill="var(--green)"/>
        <path d="M45 28 C36 28 30 22 30 14 C38 14 44 20 45 28 Z" fill="var(--green)"/>
        <path d="M45 30 C54 30 60 24 60 16 C52 16 46 22 45 30 Z" fill="var(--green)"/>
        <path d="M45 44 C34 44 26 38 26 30 C36 30 44 36 45 44 Z" fill="var(--green)"/>
        <path d="M45 46 C56 46 64 40 64 32 C54 32 46 38 45 46 Z" fill="var(--green)"/>
        <path d="M2 72 C8 60 22 56 45 58 C66 56 82 62 88 72 Z" fill="var(--green)"/>
      </svg>
      <div class="product__label">Compost + Soil + Mulch</div>
    </div>

    <div class="product product--stone">
      <svg class="product__icon" width="70" height="72" viewBox="0 0 70 72">
        <ellipse cx="35" cy="60" rx="31" ry="12" fill="var(--orange)"/>
        <ellipse cx="36" cy="40" rx="20" ry="9" fill="var(--orange)"/>
        <ellipse cx="33" cy="24" rx="13" ry="7" fill="var(--orange)"/>
        <ellipse cx="35" cy="9" rx="7" ry="7" fill="var(--orange)"/>
      </svg>
      <div class="product__label">Decorative Stone + Aggregates</div>
    </div>

    <div class="product product--trailer">
      <svg class="product__icon" width="136" height="72" viewBox="0 0 136 72">
        <rect x="48" y="4" width="86" height="40" fill="var(--green)"/>
        <path d="M2 46 H134" stroke="var(--green)" stroke-width="4"/>
        <path d="M22 30 V58" stroke="var(--green)" stroke-width="3"/>
        <circle cx="27" cy="60" r="5" fill="var(--green)"/>
        <circle cx="96" cy="54" r="14" fill="var(--green)"/>
        <circle cx="96" cy="54" r="7" fill="var(--paper)"/>
        <circle cx="96" cy="54" r="3" fill="var(--green)"/>
      </svg>
      <div class="product__label">Hire Trailer + Delivery</div>
    </div>

    <div class="tagline-band">Garden &amp; Landscape Supplies</div>
  </main>
</body>
</html>
```